All-natural soap packaging design for new company

The box type has been selected, we just need artwork for each of our 10 products. I'd like the same look to each, the idea is just to switch out the name and ingredient label on each. The dimensions are 3.5"x3.75"x1.25". The colors in the uploaded pictures with product titles are not mandatory. I'd like to keep the font on the packaging (Rubik) as it is the same as the website.

Target Market(s)

Health & Beauty, people looking for natural or organic products

Industry/Entity Type

It Company

Colors

Designer to choose colors to be used in the design.

Requirements
Must have
• Design must be clean and relatively simple. Slightly different look for each of the 10 products. Audience is people looking for all-natural products.

```html
<!DOCTYPE html>
<html lang="en">
<head>
<meta charset="utf-8">
<title>Lavender + Witch Hazel — Soap Box Artwork</title>
<link rel="stylesheet" href="https://fonts.googleapis.com/css2?family=Rubik:wght@500;700;800&display=swap">
<style>
  :root {
    --stage: #ddd0de;
    --panel-violet: #c27cc3;
    --panel-violet-deep: #a95aa9;
    --foam-light: #f6e9f4;
    --foam-mid: #e4b9e0;
    --foam-edge: #b463b3;
    --ink-white: #ffffff;
    --title-shadow: #7a3c84;
    --edge-violet: #3b2566;
    --fold-line: #4a2e6e;
    --flap-fill: #ffffff;
    --flap-outline: #e0708e;
    --tab-border: #3b3b44;
    --tab-text: #5a5a60;
    --tab-accent: #2f86d6;
    --arch-border: #3a2566;
    --arch-fill: #ffffff;
    --sprig-violet: #8a63b8;
    --sprig-green: #9bbf78;
  }
  * { margin: 0; padding: 0; box-sizing: border-box; }
  html, body {
    width: 1200px; height: 613px; overflow: hidden;
    background: var(--stage);
    font-family: "Rubik", sans-serif;
  }
  .canvas { position: relative; width: 1200px; height: 613px; }

  /* shared pieces */
  .foam {
    position: absolute; left: 0; top: 0; width: 100%;
    background: linear-gradient(180deg, var(--foam-light) 0%, var(--foam-mid) 62%, var(--foam-edge) 100%);
  }
  .field {
    position: absolute; left: 0; width: 100%; bottom: 0;
    background: linear-gradient(180deg, var(--panel-violet) 0%, var(--panel-violet-deep) 100%);
  }
  .brand-tab {
    position: absolute; background: var(--ink-white);
    border: 2px solid var(--tab-border); border-top: none;
    display: flex; flex-direction: column; align-items: center; justify-content: flex-end;
    box-shadow: 0 3px 8px rgba(60, 30, 70, 0.25);
  }
  .brand-tab__mark { background: var(--tab-accent); }
  .brand-tab__name {
    font-weight: 500; color: var(--tab-text); text-align: center;
    text-transform: uppercase; line-height: 1.1; white-space: nowrap;
  }
  .title {
    position: absolute; color: var(--ink-white); text-transform: uppercase;
    white-space: nowrap; line-height: 1;
  }
  .title--main { font-weight: 800; transform-origin: left top; }
  .title--sub { font-weight: 700; transform-origin: left top; }
  .arch {
    position: absolute; border-radius: 50%;
    background: var(--arch-fill); border: 2px solid var(--arch-border); overflow: hidden;
  }
  .arch__art {
    position: absolute; border-radius: 50% 50% 0 0;
    background: radial-gradient(ellipse at 50% 70%, var(--sprig-violet) 0%, #b59bd6 45%, var(--sprig-green) 75%, var(--arch-fill) 100%);
  }

  /* flat dieline */
  .dieline { position: absolute; left: 76px; top: 28px; width: 222px; height: 558px; }
  .dieline__flap {
    position: absolute; left: 0; top: 0; width: 222px; height: 26px;
    background: var(--flap-fill); border: 1.5px solid var(--flap-outline); border-bottom: none;
    border-radius: 18px 18px 0 0;
  }
  .dieline__body {
    position: absolute; left: 0; top: 24px; width: 222px; height: 534px;
    background: var(--edge-violet); border: 1px solid var(--flap-outline);
  }
  .dieline__face { position: absolute; left: 10px; top: 0; width: 200px; height: 100%; overflow: hidden; }
  .dieline__face .foam { height: 150px; }
  .dieline__face .field { top: 150px; }
  .dieline__upper { position: absolute; left: 0; top: 0; width: 100%; height: 266px; overflow: hidden; }
  .dieline__fold { position: absolute; left: 0; width: 100%; height: 1px; background: var(--fold-line); }
  .dieline .brand-tab { left: 78px; top: 70px; width: 46px; height: 54px; border-radius: 0 0 6px 6px; padding-bottom: 4px; gap: 4px; }
  .dieline .brand-tab__mark { width: 16px; height: 16px; }
  .dieline .brand-tab__name { font-size: 4px; }
  .dieline .title--main { left: 20px; top: 150px; font-size: 27px; transform: scaleY(1.3); text-shadow: 1px 1px 0 var(--title-shadow); }
  .dieline .title--sub { left: 54px; top: 188px; font-size: 12px; text-shadow: 1px 1px 0 var(--title-shadow); }
  .dieline .arch { left: 48px; top: 216px; width: 104px; height: 104px; }
  .dieline .arch__art { left: 8px; top: 8px; width: 86px; height: 44px; }

  /* front panel */
  .front { position: absolute; left: 410px; top: 72px; width: 522px; height: 480px; }
  .front__edge { position: absolute; top: 0; width: 12px; height: 100%; background: var(--edge-violet); }
  .front__edge--left { left: 0; }
  .front__edge--right { right: 0; }
  .front__face { position: absolute; left: 12px; top: 0; width: 498px; height: 480px; overflow: hidden; }
  .front__face .foam { height: 196px; }
  .front__face .field { top: 196px; }
  .front .brand-tab { left: 180px; top: 18px; width: 112px; height: 130px; border-radius: 0 0 14px 14px; padding-bottom: 10px; gap: 10px; }
  .front .brand-tab__mark { width: 34px; height: 34px; }
  .front .brand-tab__name { font-size: 10px; }
  .front .title--main { left: 42px; top: 200px; font-size: 64px; transform: scaleY(1.35); text-shadow: 3px 3px 0 var(--title-shadow); }
  .front .title--sub { left: 120px; top: 280px; font-size: 30px; text-shadow: 2px 2px 0 var(--title-shadow); }
  .front .arch { left: 100px; top: 344px; width: 278px; height: 278px; }
  .front .arch__art { left: 18px; top: 18px; width: 238px; height: 116px; }
</style>
</head>
<body>
<main class="canvas">

  <section class="dieline" aria-label="Flat box wrap">
    <div class="dieline__flap"></div>
    <div class="dieline__body">
      <div class="dieline__face">
        <div class="dieline__upper">
          <div class="foam" role="img" aria-label="Photograph of lavender-tinted soap foam bubbles"></div>
          <div class="field" role="img" aria-label="Violet field with a scattered small dash pattern"></div>
          <div class="brand-tab">
            <span class="brand-tab__mark"></span>
            <span class="brand-tab__name">Birchwell Soap Co.</span>
          </div>
          <div class="title title--main">Lavender +</div>
          <div class="title title--sub">Witch Hazel</div>
          <div class="arch">
            <div class="arch__art" role="img" aria-label="Illustration of lavender sprigs and green leaves arranged in an arch"></div>
          </div>
        </div>
        <div class="field" style="top:266px" role="img" aria-label="Violet field with a scattered small dash pattern"></div>
        <div class="dieline__fold" style="top:70px"></div>
        <div class="dieline__fold" style="top:266px"></div>
        <div class="dieline__fold" style="top:334px"></div>
        <div class="dieline__fold" style="top:526px"></div>
      </div>
    </div>
  </section>

  <section class="front" aria-label="Box front panel">
    <div class="front__edge front__edge--left"></div>
    <div class="front__face">
      <div class="foam" role="img" aria-label="Photograph of lavender-tinted soap foam bubbles"></div>
      <div class="field" role="img" aria-label="Violet field with a scattered small dash pattern"></div>
      <div class="brand-tab">
        <span class="brand-tab__mark"></span>
        <span class="brand-tab__name">Birchwell Soap Co.</span>
      </div>
      <h1 class="title title--main">Lavender +</h1>
      <p class="title title--sub">Witch Hazel</p>
      <div class="arch">
        <div class="arch__art" role="img" aria-label="Illustration of lavender sprigs and green leaves arranged in an arch"></div>
      </div>
    </div>
    <div class="front__edge front__edge--right"></div>
  </section>

</main>
</body>
</html>
```